Growing Your Label eBook Cover Design

I want to deisgn a cover for my eBook (FRONT COVER) and the title is:

Why I Grew a Six-Figure Label. So You Should Start
By KL Baxter

TITLE CHANGED TO: OUT OF DEBT INTO POWER; WHY I GREW A NINE-FIGURE FORTUNE SO YOU SHOULD START

The color palette is attached. Along with some photos options of me. Along with the ebook in WORD Document. My website is www.KLBaXterHub.com. You can use a different color palette if you think it is best

Target Market(s)

women who look to build a personal brand

Industry/Entity Type

health and wellness

Requirements
Must have
• the title
Nice to have
• use my picture on the cover; but that is optional
Should not have
• any men

```html
<!DOCTYPE html>
<html lang="en">
<head>
<meta charset="utf-8">
<title>Out of Debt Into Power — KL Baxter</title>
<link rel="stylesheet" href="https://fonts.googleapis.com/css2?family=Caveat:wght@400;500&family=Oswald:wght@700&family=Montserrat:wght@700&family=Quicksand:wght@300&display=swap">
<style>
  :root {
    --plum: #4a3d5a;
    --orchid: #d9aed0;
    --mint: #1bc48a;
    --white: #ffffff;
    --photo-dark: #2a2530;
    --photo-light: #8a6f6a;
  }
  * { margin: 0; padding: 0; box-sizing: border-box; }
  html, body { width: 840px; height: 1200px; overflow: hidden; }
  body { background: var(--orchid); }
  .cover {
    position: relative;
    width: 840px;
    height: 1200px;
    background: var(--orchid);
    overflow: hidden;
  }
  .cover__panel {
    position: absolute;
    left: 0; top: 0;
    width: 467px; height: 1200px;
    background: var(--plum);
  }
  .cover__portrait {
    position: absolute;
    left: 382px; top: 70px;
    width: 458px; height: 1130px;
    border-radius: 200px 200px 0 0;
    background: linear-gradient(180deg, var(--photo-light) 0%, var(--photo-dark) 28%, var(--photo-dark) 100%);
  }
  .title { position: absolute; left: 0; top: 0; width: 840px; height: 1200px; }
  .title span { position: absolute; white-space: nowrap; line-height: 1; }
  .script { font-family: "Caveat", cursive; color: var(--white); font-weight: 500; }
  .title__lead { left: 44px; top: 112px; font-size: 80px; }
  .title__power {
    left: 52px; top: 196px;
    font-family: "Oswald", sans-serif; font-weight: 700;
    font-size: 118px; color: var(--orchid); letter-spacing: 0; line-height: 1;
    transform: scaleX(0.86); transform-origin: left top;
  }
  .title__how { left: 48px; top: 362px; font-size: 72px; }
  .title__figure, .title__fortune {
    font-family: "Oswald", sans-serif; font-weight: 700; text-transform: uppercase;
  }
  .title__figure { left: 48px; top: 446px; font-size: 106px; color: var(--white); transform: scaleX(0.9); transform-origin: left top; }
  .title__fortune { left: 48px; top: 548px; font-size: 124px; color: var(--mint); }
  .title__and {
    left: 190px; top: 678px;
    font-family: "Quicksand", sans-serif; font-weight: 300;
    font-size: 62px; color: var(--white); font-style: italic;
  }
  .title__you {
    left: 46px; top: 736px;
    font-family: "Montserrat", sans-serif; font-weight: 700;
    font-size: 114px; color: var(--orchid);
  }
  .title__start {
    left: 48px; top: 846px;
    font-family: "Montserrat", sans-serif; font-weight: 700;
    font-size: 56px; color: var(--white);
  }
  .byline {
    position: absolute; left: 48px; top: 912px;
    font-family: "Quicksand", sans-serif; font-weight: 300;
    font-size: 34px; color: var(--white);
  }
  .author {
    position: absolute; left: 48px; top: 960px;
    font-family: "Caveat", cursive; font-weight: 500;
    font-size: 76px; color: var(--white); line-height: 1;
  }
</style>
</head>
<body>
  <main class="cover">
    <div class="cover__panel"></div>
    <div class="cover__portrait" role="img" aria-label="Portrait of the author smiling, in a black turtleneck and trousers"></div>
    <h1 class="title">
      <span class="script title__lead">Out of Debt</span>
      <span class="title__power">INTO POWER;</span>
      <span class="script title__how">why i Grew a</span>
      <span class="title__figure">NINE-FIGURE</span>
      <span class="title__fortune">FORTUNE</span>
      <span class="title__and">so</span>
      <span class="title__you">YOU</span>
      <span class="title__start">SHOULD START</span>
    </h1>
    <p class="byline">by</p>
    <p class="author">KL Baxter</p>
  </main>
</body>
</html>
```